Summer Drinks Flyer for Coffee Shop

We are a coffee shop in London and would like to have a cool and nice flyer for our summer drinks (juices and frozen drink) flyer - see on the attached file for the list

Attached you can find an "attempt" - please note that I would no necessary need the image below.

I also attache our new logo.

thank you

Industry/Entity Type

Coffee Shop

```html
<!DOCTYPE html>
<html lang="en">
<head>
<meta charset="utf-8">
<title>Soleluna – New Summer Drinks Menu</title>
<link href="https://fonts.googleapis.com/css2?family=Arimo:wght@400&family=Delius&family=Sniglet:wght@800&display=swap" rel="stylesheet">
<style>
  :root {
    --backdrop: #5e5e5e;
    --gold: #b8962f;
    --gold-deep: #a9862a;
    --glow: #fbf6e2;
    --ink: #1e1a12;
    --white: #ffffff;
    --swoosh: #c9c9c9;
    --swoosh-dark: #9a9a9a;
    --fruit-red: #c8322d;
    --fruit-orange: #f2a21c;
    --fruit-blue: #3bb4e0;
  }
  * { margin: 0; padding: 0; box-sizing: border-box; }
  html, body {
    width: 913px; height: 1200px; overflow: hidden;
    background: var(--backdrop);
  }
  .flyer {
    position: absolute; left: 30px; top: 28px;
    width: 856px; height: 1144px;
    background: var(--gold);
    overflow: hidden;
  }
  .menu-glow {
    position: absolute; left: 42px; top: 672px;
    width: 770px; height: 440px; border-radius: 50%;
    background: radial-gradient(ellipse at center, var(--glow) 0%, #efe0a8 45%, rgba(184,150,47,0) 75%);
  }
  .brand {
    position: absolute; left: 38px; top: 96px;
    font-family: "Arimo", sans-serif; font-weight: 400;
    font-size: 52px; letter-spacing: 1px;
    color: var(--white);
  }
  .hero { position: absolute; left: 0; top: 0; }
  .menu-title {
    position: absolute; left: 0; right: 0; top: 672px;
    text-align: center;
    font-family: "Sniglet", sans-serif; font-weight: 800;
    font-size: 44px; color: var(--white);
    text-shadow: 2px 3px 3px rgba(60,40,0,.55);
  }
  .menu { position: absolute; left: 50px; width: 760px; }
  .menu-item { margin-bottom: 28px; }
  .item-line {
    display: flex; align-items: baseline;
    font-family: "Delius", cursive; font-size: 22px; color: var(--ink);
  }
  .item-name { white-space: nowrap; }
  .item-leader {
    flex: 1; border-bottom: 2px dotted var(--ink);
    margin: 0 2px; transform: translateY(-5px);
  }
  .item-price { font-family: "Arimo", sans-serif; font-size: 23px; }
  .item-options {
    text-align: center; font-family: "Arimo", sans-serif;
    font-size: 19px; line-height: 28px; color: var(--ink);
  }
  .item-note { font-size: 14px; }
  .contact {
    position: absolute; left: 0; right: 0; top: 1062px;
    text-align: center; font-family: "Arimo", sans-serif;
    font-size: 48px; color: var(--ink);
  }
</style>
</head>
<body>
<main class="flyer">
  <div class="menu-glow"></div>

  <svg class="hero" width="856" height="680" viewBox="0 0 856 680">
    <defs>
      <linearGradient id="fruitTones" x1="0" y1="0" x2="1" y2="0">
        <stop offset="0" stop-color="var(--fruit-orange)"/>
        <stop offset="0.25" stop-color="var(--fruit-red)"/>
        <stop offset="0.48" stop-color="var(--fruit-orange)"/>
        <stop offset="0.66" stop-color="var(--fruit-blue)"/>
        <stop offset="0.85" stop-color="#7a9a3a"/>
        <stop offset="1" stop-color="#8c2a34"/>
      </linearGradient>
      <linearGradient id="swooshTone" x1="0" y1="0" x2="1" y2="0">
        <stop offset="0" stop-color="var(--swoosh-dark)"/>
        <stop offset="0.5" stop-color="var(--swoosh)"/>
        <stop offset="1" stop-color="var(--white)"/>
      </linearGradient>
    </defs>
    <path role="img" aria-label="Photo of three glasses of red, orange and blue summer drinks among watermelon, cherries, grapes and tropical fruit"
          d="M0,352 C250,205 520,118 856,132 L856,482 C600,560 300,592 0,588 Z"
          fill="url(#fruitTones)"/>
    <path d="M0,318 C250,160 520,98 856,116 L856,134 C520,118 250,205 0,355 Z" fill="url(#swooshTone)"/>
    <path d="M0,322 C250,166 520,104 856,120" fill="none" stroke="var(--white)" stroke-width="3"/>
    <path d="M0,588 C300,592 600,560 856,482 L856,520 C600,602 300,632 0,628 Z" fill="url(#swooshTone)"/>
  </svg>

  <div class="brand">soleluna</div>

  <h1 class="menu-title">New Summer Drinks Menu</h1>

  <section class="menu" style="top:764px;">
    <div class="menu-item">
      <div class="item-line"><span class="item-name">Frozen Fruit Drinks</span><span class="item-leader"></span><span class="item-price">£2.95</span></div>
      <p class="item-options">Strawberry and banana | Pineapple, mango and banana</p>
    </div>
    <div class="menu-item" style="margin-top:22px;">
      <div class="item-line" style="padding-left:14px;"><span class="item-leader"></span><span class="item-price">£2.95</span></div>
      <p class="item-options">Orange and carrot | Orange and pineapple | Pineapple and apple Apple and<br>kiwi Carrot and ginger <span class="item-note">(Add Mint or Ginger for Free!)</span></p>
    </div>
    <div class="menu-item">
      <div class="item-line"><span class="item-name">Iced-Coffees</span><span class="item-leader"></span><span class="item-price">£2.45</span></div>
      <p class="item-options">Iced Coffee | Iced Latte | Iced Chocolate Drink <span class="item-note">(Add Syrup shot for 10p)</span></p>
    </div>
  </section>

  <p class="contact">Your Contact info here</p>
</main>
</body>
</html>
```